Velmora Jewellery 25% off pinwheelr like business card

I need a business card designed, the card will be used to send with sold items from the stores.
Theme is black and gold like the logo and name (see pictures)
Must have the following:

Velmora Jewellery logo front and back (use pictures)

www.velmorajewellery-example.com
shops.bazaarvane.com.au/Velmora-Jewellery
info@velmorajewellery-example.com

Like us on pinwheelr for 25% OFF your next purchase!

FREE shipping worldwide!

```html
<!DOCTYPE html>
<html lang="en">
<head>
<meta charset="utf-8">
<title>Velmora Jewellery – Business Card</title>
<link rel="stylesheet" href="https://fonts.googleapis.com/css2?family=Montserrat:wght@300;400;600;700&family=Open+Sans:wght@600;700&display=swap">
<style>
  :root {
    --backdrop: #b9b9b9;
    --card-black: #0b0b0b;
    --gold: #c9a36a;
    --gold-light: #e6c995;
    --gold-deep: #8a6a3c;
    --ink-white: #f4f4f4;
  }
  * { box-sizing: border-box; margin: 0; padding: 0; }
  html, body { width: 1200px; height: 896px; overflow: hidden; }
  body {
    background: var(--backdrop);
    font-family: "Open Sans", Arial, sans-serif;
    display: flex; flex-direction: column; align-items: center; justify-content: center;
    gap: 40px;
  }
  .card {
    position: relative; width: 700px; height: 400px;
    background: var(--card-black); overflow: hidden;
    box-shadow: 0 6px 18px rgba(0,0,0,.25);
  }
  .card-edge { position: absolute; top: 0; left: 0; width: 700px; height: 400px; }
  .gold-tab {
    position: absolute;
    background: linear-gradient(135deg, var(--gold-light), var(--gold) 55%, var(--gold-deep));
  }
  .front .gold-tab { left: 0; top: 196px; width: 62px; height: 52px; }
  .back .gold-tab { right: 0; top: 300px; width: 26px; height: 48px; }

  .logo-ring { position: absolute; border: 2px solid var(--gold); border-radius: 50%; }
  .wordmark {
    font-family: "Montserrat", Arial, sans-serif; font-weight: 300;
    color: var(--gold); text-transform: uppercase; letter-spacing: 6px; line-height: 1.25;
  }
  .front .logo-ring { left: 112px; top: 60px; width: 104px; height: 104px; }
  .front .wordmark { position: absolute; left: 236px; top: 90px; font-size: 26px; }

  .holder { position: absolute; left: 84px; top: 196px; }
  .holder-name {
    font-family: "Montserrat", Arial, sans-serif; font-weight: 700;
    color: var(--gold); font-size: 31px; letter-spacing: 1px; line-height: 1.1;
  }
  .holder-role {
    font-family: "Montserrat", Arial, sans-serif; font-weight: 400;
    color: var(--ink-white); font-size: 16px; letter-spacing: 5px; margin-top: 4px;
  }

  .contact-list { position: absolute; left: 330px; top: 266px; list-style: none; }
  .contact-list li {
    display: flex; align-items: flex-start; gap: 12px;
    color: var(--ink-white); font-weight: 700; font-size: 13px; line-height: 16px; margin-bottom: 5px;
  }
  .contact-list svg { flex: none; width: 16px; height: 16px; fill: var(--gold); }

  .back .logo-ring {
    left: 290px; top: 64px; width: 120px; height: 120px;
    display: flex; align-items: center; justify-content: center; text-align: center;
  }
  .back .wordmark { font-size: 12px; letter-spacing: 3px; }
  .promo { position: absolute; left: 0; right: 0; top: 206px; text-align: center; }
  .promo-offer {
    font-family: "Montserrat", Arial, sans-serif; font-weight: 600;
    color: var(--gold); font-size: 17px; letter-spacing: .5px;
  }
  .promo-shipping {
    font-family: "Montserrat", Arial, sans-serif; font-weight: 400;
    color: var(--ink-white); font-size: 13px; letter-spacing: 4px; margin-top: 8px; text-transform: uppercase;
  }
  .social-row {
    position: absolute; left: 56px; right: 56px; top: 318px;
    display: flex; justify-content: space-between; list-style: none;
  }
  .social-row li { display: flex; align-items: baseline; gap: 10px; font-size: 15px; }
  .network { color: var(--gold); font-weight: 700; }
  .handle { color: var(--ink-white); font-weight: 600; }
</style>
</head>
<body>

  <section class="card front" aria-label="Card front">
    <svg class="card-edge" viewBox="0 0 700 400" aria-hidden="true">
      <defs>
        <linearGradient id="edgeGoldFront" x1="0" x2="1" y1="0" y2="0">
          <stop offset="0" stop-color="#8a6a3c"/><stop offset=".6" stop-color="#e6c995"/><stop offset="1" stop-color="#c9a36a"/>
        </linearGradient>
      </defs>
      <path d="M0 0 H700 V26 Q420 4 0 0 Z" fill="url(#edgeGoldFront)"/>
    </svg>
    <div class="gold-tab"></div>
    <div class="logo-ring"></div>
    <div class="wordmark">Velmora<br>Jewellery</div>

    <div class="holder">
      <p class="holder-name">ELIAS MARVELL</p>
      <p class="holder-role">GENERAL MANAGER</p>
    </div>

    <ul class="contact-list">
      <li>
        <svg viewBox="0 0 24 24"><path d="M12 3 2 12h3v9h5v-6h4v6h5v-9h3z"/></svg>
        <span>214 Harbour Crest, Level 6<br>Kestrel Road NKD</span>
      </li>
      <li>
        <svg viewBox="0 0 24 24"><path d="M12 2a10 10 0 1 0 0 20 10 10 0 0 0 0-20zm0 2c1.2 1.4 2 3.5 2.2 6H9.8c.2-2.5 1-4.6 2.2-6zM4.1 13h3.7c.1 2 .6 3.9 1.4 5.4A8 8 0 0 1 4.1 13zm3.7-2H4.1a8 8 0 0 1 5.1-6.4c-.8 1.5-1.3 3.4-1.4 6.4zm2 2h4.4c-.2 2.5-1 4.6-2.2 6-1.2-1.4-2-3.5-2.2-6zm5 5.4c.8-1.5 1.3-3.4 1.4-5.4h3.7a8 8 0 0 1-5.1 5.4zm1.4-7.4c-.1-3-.6-4.9-1.4-6.4a8 8 0 0 1 5.1 6.4z"/></svg>
        <span>www.velmorajewellery-example.com</span>
      </li>
      <li>
        <svg viewBox="0 0 24 24"><path d="M4 4h16l-1.5 6H5.5zM5 12h14v8H5zm5 2v4h4v-4z"/></svg>
        <span>shops.bazaarvane.com.au/Velmora-Jewellery</span>
      </li>
      <li>
        <svg viewBox="0 0 24 24"><path d="M2 5h20v14H2zm2 2v.5l8 5.5 8-5.5V7zm0 3v7h16v-7l-8 5.5z"/></svg>
        <span>info@velmorajewellery-example.com</span>
      </li>
      <li>
        <svg viewBox="0 0 24 24"><path d="M6.6 10.8a15 15 0 0 0 6.6 6.6l2.2-2.2c.3-.3.7-.4 1-.2 1.1.4 2.3.6 3.6.6.6 0 1 .4 1 1V20c0 .6-.4 1-1 1A17 17 0 0 1 3 4c0-.6.4-1 1-1h3.5c.6 0 1 .4 1 1 0 1.3.2 2.5.6 3.6.1.3 0 .7-.2 1z"/></svg>
        <span>013 555 0192</span>
      </li>
    </ul>
  </section>

  <section class="card back" aria-label="Card back">
    <svg class="card-edge" viewBox="0 0 700 400" aria-hidden="true">
      <defs>
        <linearGradient id="edgeGoldBack" x1="0" x2="1" y1="0" y2="0">
          <stop offset="0" stop-color="#8a6a3c"/><stop offset=".5" stop-color="#e6c995"/><stop offset="1" stop-color="#c9a36a"/>
        </linearGradient>
      </defs>
      <path d="M260 0 H700 V40 Q560 6 260 0 Z" fill="url(#edgeGoldBack)"/>
    </svg>
    <div class="gold-tab"></div>
    <div class="logo-ring"><span class="wordmark">Velmora<br>Jewellery</span></div>

    <div class="promo">
      <p class="promo-offer">Like us on pinwheelr for 25% OFF your next purchase!</p>
      <p class="promo-shipping">FREE shipping worldwide!</p>
    </div>

    <ul class="social-row">
      <li><span class="network">linkvista</span><span class="handle">yourname</span></li>
      <li><span class="network">chirpline</span><span class="handle">@yourname</span></li>
      <li><span class="network">pinwheelr</span><span class="handle">yourname</span></li>
    </ul>
  </section>

</body>
</html>
```